Wordpress Design Project (Dorvane)

We need a wordpress design for an established auction and real estate company based in New Jersey. The winning design will incorporate a professional color scheme and company logo in a clean layout.

Industry/Entity Type

Real Estate

Requirements
Must have
• - We will require winning designer to provide a layered PSD (Adobe photoshop) concept file, along with any non-standard font files used.

Logo attached. Will hopefully post better logo shortly. Please use site design colors of your choice as the logo is black & white. A site client mentions liking is http://www.plxbidhouse.example/. Homepage content will be an auction list as seen at http://www.ridgelinesaleindex.example/?page=5

Horizontal Navigation menu with these pages:
Home - Auction Calendar - Appraisals - Services - Company Profile - News & Events - Testimonials - Contact Us

A slideshow element on the home page using one of the placeholder images provided (or stock if higher resolution image is necessary).

Sidebar widgets to be included are: Email sign-up form - Featured Auctions - Testimonial widget - 'Our Videos' widget; Social media icons somewhere in layout (facebook, twitter, RSS, and Youtube)

Homepage content is text:
DORVANE OVERSIGHT COMPANY was founded 90 years ago in 1921 by Harold Dorvane, which makes us one of the oldest commercial and industrial auction and appraisal companies in America.

We have conducted thousands of auctions, assisting a wide range of companies both large and small achieve maximum value for their capital assets.
Nice to have
• - Site will have drop down menus, nice to have a sample look for them on one of the primary menu items.

```html
<!DOCTYPE html>
<html lang="en">
<head>
<meta charset="utf-8">
<title>Dorvane – Home</title>
<link href="https://fonts.googleapis.com/css2?family=Open+Sans:wght@400;600;700&display=swap" rel="stylesheet">
<style>
:root{
  --ink:#222;
  --text:#555;
  --muted:#888;
  --line:#d9d9d9;
  --panel:#f3f3f3;
  --dark:#2c2c2c;
  --darker:#1f1f1f;
  --nav-active:#4a4a4a;
  --white:#fff;
  --photo-red:#9b2b2b;
  --photo-sky:#7fa9c9;
}
*{box-sizing:border-box;margin:0;padding:0}
html,body{width:867px;height:1200px;overflow:hidden}
body{font-family:"Open Sans",Arial,sans-serif;color:var(--text);background:var(--white);font-size:10px;position:relative}
.abs{position:absolute}

.logo{left:29px;top:14px;width:132px;height:44px;border:2px solid var(--ink);display:flex;align-items:center;gap:6px;padding:0 8px}
.logo-mark{width:18px;height:18px;background:var(--ink)}
.logo-name{font-weight:700;font-size:17px;color:var(--ink);letter-spacing:.5px}
.search{left:613px;top:44px;width:225px;height:20px;border:1px solid var(--line);background:var(--white);display:flex;align-items:center;justify-content:space-between;padding:0 6px;color:var(--muted);font-size:9px}

.nav{left:29px;top:82px;width:809px;height:28px;background:linear-gradient(#3a3a3a,var(--darker));display:flex}
.nav a{color:#ddd;text-decoration:none;font-size:10px;padding:0 14px;line-height:28px}
.nav a.active{background:var(--nav-active);color:var(--white)}

.slider{left:29px;top:127px;width:578px;height:200px;background:linear-gradient(180deg,var(--photo-sky) 0%,#b8c9d6 40%,var(--photo-red) 60%,#5d3232 100%)}
.slider-bar{left:29px;top:304px;width:578px;height:23px;background:rgba(20,20,20,.85);display:flex;align-items:center;padding:0 8px;color:#ccc;font-size:9px;gap:10px}
.slider-bar strong{color:var(--white);font-size:10px}
.slider-arrows{margin-left:auto;display:flex;gap:3px}
.slider-arrows span{width:16px;height:16px;background:#555;color:#fff;display:flex;align-items:center;justify-content:center;font-size:9px}

.contact{left:613px;top:127px;width:225px;height:75px;background:var(--dark);color:var(--white);text-align:center;padding-top:8px}
.contact .label{font-size:11px;color:#ccc}
.contact .phone{font-size:17px;font-weight:700;margin-top:2px}
.contact .email{font-size:11px;font-weight:600}
.mailing{left:613px;top:208px;width:225px;height:58px;background:var(--dark);color:var(--white);padding:7px 10px}
.mailing h4{font-size:11px;font-weight:600;display:flex;align-items:center;gap:6px}
.mailing .check{width:12px;height:12px;background:var(--white)}
.mailing form{display:flex;gap:4px;margin-top:8px}
.mailing .field{flex:1;height:17px;background:var(--white);color:var(--muted);font-size:8px;padding:3px}
.mailing .btn{height:17px;padding:0 6px;background:#555;font-size:8px;line-height:17px}

h2{font-size:13px;font-weight:700;color:var(--ink)}
.welcome{left:29px;top:342px;width:578px}
.welcome p{font-size:9.5px;line-height:14px;margin-top:6px}
.rule{height:1px;background:var(--line);margin-top:8px}

.videos{left:613px;top:341px;width:225px;height:136px;background:var(--dark)}
.videos h3{color:var(--white);font-size:11px;font-weight:600;padding:6px 10px}
.video-frame{margin:0 10px;height:96px;background:linear-gradient(#444,#2a2a2a);display:flex;align-items:center;justify-content:center}

.latest{left:29px;top:498px;width:578px}
.auction{width:578px;height:178px;border:1px solid var(--line);margin-top:10px}
.auction-head{height:28px;background:var(--panel);display:flex;align-items:center;justify-content:space-between;padding:0 10px;font-size:10px;color:var(--ink);font-weight:600}
.auction-head .icons{display:flex;gap:8px}
.auction-body{display:flex;padding:12px 10px;gap:12px}
.auction-photo{width:118px;height:90px;background:linear-gradient(180deg,#9cb6cb 0%,#cfd8de 45%,#8a3030 70%,#555 100%);flex:none}
.auction-text p{font-size:8.5px;line-height:12px}
.auction-text .meta{font-size:10.5px;color:var(--ink);margin-top:8px;line-height:16px}

.pager{left:170px;top:1096px;display:flex;gap:3px}
.pager span{width:12px;height:12px;background:#ccc}
.pager span.on{background:var(--dark)}

.featured{left:613px;top:498px;width:225px}
.feat{display:flex;gap:8px;padding:9px 0;border-bottom:1px solid var(--line)}
.feat-photo{width:64px;height:52px;background:linear-gradient(180deg,#a9bfcf,#8b2e2e 70%,#4a4a4a);flex:none}
.feat p{font-size:8px;line-height:11px}
.feat .date{color:var(--muted);font-size:7.5px;margin-top:3px}

.testi{left:613px;top:858px;width:225px}
.quote{margin-top:10px;border:1px solid var(--line);padding:12px 12px 12px 30px;position:relative;font-size:9px;line-height:14px;font-style:italic}
.quote .mark{position:absolute;left:10px;top:6px;font-size:22px;color:var(--ink);font-style:normal}
.by{text-align:right;font-size:8.5px;margin-top:6px;color:var(--text)}

.footer{left:0;top:1130px;width:867px;height:70px;background:var(--dark);color:#bbb;font-size:8.5px;padding:14px 29px}
.footer nav{display:flex;gap:8px}
.footer .copy{margin-top:8px;color:#999}
.social{position:absolute;right:29px;top:16px;display:flex;gap:4px}
.social span{width:18px;height:18px;background:#555}
</style>
</head>
<body>

<div class="abs logo"><span class="logo-mark"></span><span class="logo-name">DORVANE</span></div>
<div class="abs search"><span>Search</span>
<svg width="10" height="10" viewBox="0 0 10 10"><circle cx="4" cy="4" r="3" fill="none" stroke="#888" stroke-width="1.3"/><line x1="6.3" y1="6.3" x2="9.3" y2="9.3" stroke="#888" stroke-width="1.3"/></svg></div>

<nav class="abs nav">
  <a class="active">Home</a><a>Auction Calendar</a><a>Appraisals</a><a>Services</a><a>Company Profile</a><a>News &amp; Events</a><a>Testimonials</a><a>Contact Us</a>
</nav>

<div class="abs slider" role="img" aria-label="Row of red trucks parked under a blue sky"></div>
<div class="abs slider-bar"><strong>Upcoming Auctions</strong><span>Praesent gravida metus a condimentum convallis</span>
<span class="slider-arrows"><span>&#9664;</span><span>&#9654;</span></span></div>

<div class="abs contact"><div class="label">Contact us</div><div class="phone">(800) 555 - 0142</div><div class="email">info@dorvane.example</div></div>
<div class="abs mailing"><h4><span class="check"></span>Join our Mailing List</h4>
<form><span class="field">Email ID...</span><span class="btn">SUBMIT</span></form></div>

<section class="abs welcome">
<h2>Welcome to Dorvane</h2>
<p>DORVANE OVERSIGHT COMPANY was founded 90 years ago in 1921 by Harold Dorvane, which makes us one of the oldest commercial and industrial auction and appraisal companies in America.</p>
<p>We have conducted thousands of auctions, assisting a wide range of companies both large and small achieve maximum value for their capital assets.</p>
<div class="rule"></div>
</section>

<aside class="abs videos"><h3>Our Videos</h3>
<div class="video-frame"><svg width="34" height="34" viewBox="0 0 34 34"><circle cx="17" cy="17" r="16" fill="#777"/><polygon points="13,10 25,17 13,24" fill="#fff"/></svg></div></aside>

<section class="abs latest">
<h2>Latest Auctions</h2>
<article class="auction"><div class="auction-head">Real Estate, Equipment, &amp; Vehicles<span class="icons"><svg width="14" height="12"><rect x="1" y="1" width="12" height="10" fill="none" stroke="#777"/><line x1="1" y1="4" x2="13" y2="4" stroke="#777"/></svg><svg width="14" height="12"><path d="M1 1h12v7H6l-3 3V8H1z" fill="none" stroke="#777"/></svg></span></div>
<div class="auction-body"><div class="auction-photo" role="img" aria-label="Trucks lined up at an auction yard"></div>
<div class="auction-text"><p>Curabitur luctus dignissim velit. Donec in consequat metus. Aenean lectus ligula, viverra vitae dui id, adipiscing posuere nisl. Ut consectetur, ipsum sit amet dignissim porta, nunc turpis tincidunt quam, tincidunt luctus nunc.</p>
<div class="meta">Begins: Saturday, August 10, 2013 at 10:00 AM EDT<br>Location: 782 Larkmoor Road, Fenwick, VA 24999</div></div></div></article>
<article class="auction"><div class="auction-head">Real Estate, Equipment, &amp; Vehicles<span class="icons"><svg width="14" height="12"><rect x="1" y="1" width="12" height="10" fill="none" stroke="#777"/><line x1="1" y1="4" x2="13" y2="4" stroke="#777"/></svg><svg width="14" height="12"><path d="M1 1h12v7H6l-3 3V8H1z" fill="none" stroke="#777"/></svg></span></div>
<div class="auction-body"><div class="auction-photo" role="img" aria-label="Trucks lined up at an auction yard"></div>
<div class="auction-text"><p>Curabitur luctus dignissim velit. Donec in consequat metus. Aenean lectus ligula, viverra vitae dui id, adipiscing posuere nisl. Ut consectetur, ipsum sit amet dignissim porta, nunc turpis tincidunt quam, tincidunt luctus nunc.</p>
<div class="meta">Begins: Saturday, August 10, 2013 at 10:00 AM EDT<br>Location: 782 Larkmoor Road, Fenwick, VA 24999</div></div></div></article>
<article class="auction"><div class="auction-head">Real Estate, Equipment, &amp; Vehicles<span class="icons"><svg width="14" height="12"><rect x="1" y="1" width="12" height="10" fill="none" stroke="#777"/><line x1="1" y1="4" x2="13" y2="4" stroke="#777"/></svg><svg width="14" height="12"><path d="M1 1h12v7H6l-3 3V8H1z" fill="none" stroke="#777"/></svg></span></div>
<div class="auction-body"><div class="auction-photo" role="img" aria-label="Trucks lined up at an auction yard"></div>
<div class="auction-text"><p>Curabitur luctus dignissim velit. Donec in consequat metus. Aenean lectus ligula, viverra vitae dui id, adipiscing posuere nisl. Ut consectetur, ipsum sit amet dignissim porta, nunc turpis tincidunt quam, tincidunt luctus nunc.</p>
<div class="meta">Begins: Saturday, August 10, 2013 at 10:00 AM EDT<br>Location: 782 Larkmoor Road, Fenwick, VA 24999</div></div></div></article>
</section>

<div class="abs pager"><span></span><span></span><span class="on"></span><span></span><span></span><span></span><span></span><span></span><span></span><span></span></div>

<aside class="abs featured">
<h2>Featured Auctions</h2>
<div class="feat"><div class="feat-photo" role="img" aria-label="Red truck at auction"></div><div><p>Nulla adipiscing tellus leo, eget sollic itudin nunc venenatis</p><p class="date">Aug 8 2013</p></div></div>
<div class="feat"><div class="feat-photo" role="img" aria-label="Red truck at auction"></div><div><p>Nulla adipiscing tellus leo, eget sollic itudin nunc venenatis</p><p class="date">Aug 8 2013</p></div></div>
<div class="feat"><div class="feat-photo" role="img" aria-label="Red truck at auction"></div><div><p>Nulla adipiscing tellus leo, eget sollic itudin nunc venenatis</p><p class="date">Aug 8 2013</p></div></div>
<div class="feat"><div class="feat-photo" role="img" aria-label="Red truck at auction"></div><div><p>Nulla adipiscing tellus leo, eget sollic itudin nunc venenatis</p><p class="date">Aug 8 2013</p></div></div>
</aside>

<aside class="abs testi">
<h2>Customer's Testimonials</h2>
<div class="quote"><span class="mark">&#8220;</span>Curabitur a enim interdum, facilisis dolor in, suscipit magna. Duis aliquam tempor lobortis. Praesent gravida metus a condimentum convallis. Etiam at tellus quis diam non sollicitudin.</div>
<p class="by">Customer name, City</p>
</aside>

<footer class="abs footer">
<nav><span>Home</span>|<span>Auction Calendar</span>|<span>Appraisals</span>|<span>Services</span>|<span>Company Profile</span>|<span>News &amp; Events</span>|<span>Testimonials</span>|<span>Contact Us</span></nav>
<p class="copy">Copyright &copy; 2013 Dorvane. All rights reserved</p>
<div class="social"><span></span><span></span><span></span><span></span></div>
</footer>

</body>
</html>
```